Web Design Project: Facility Management company

Hi! We need a new website.

Our current website: http://www.brantel-group.ru/ and we don-t like it. =)
The structure of our company has changed and now we don't need "cleaning" and "engeneering" on this site.

We are facility management company in Russia. So we provide integrated service solutions specific to industrial services: maintenance, repair, etc. of engineering systems.
More services:
Energy planning
Automation
Audit
Statements with regulators
Video surveillance
Central heating
Security systems
Welding
Management of subcontractors
Electrical installation and service needs
Reception
Catering

Visitors:
* Managers in the field of commercial real estate
* Chief engineers
* TOP managers of large companies, malls, factories...
+ their subordinates
* Small% of applicants.

Here you can see some websites/patterns we liked:
http://www.kvelmort.ru/ (This is our competitor’s site, so our site shouldn’t be an exact copy))))
http://www.orbitask.ru/
http://www.layoutpinery.com/demo/24296.html
http://www.layoutpinery.com/website-templates/10145.html

Style:
Light, hi-tech/minimalizm, the color palette should be based on the original site colors (Green + black + white). http://www.brantel-group.ru/

Estimated sitemap:
1. Home
2. About Us
3. Company's policy
4. History + Achievements.
5. Certificates
6. Map of presence (Here you can use sample map in file "our projects")
7. Services
8. Portfolio
9. News or blog
10. Jobs
11. Contacts - with the feedback form (or the function "call to order")
12. English

Need a design pages: main page, page 404. The rest of the page could be created by general pattern.

Logo, navigation bar and contacts should be visible on all pages of a site.
Flash animation elements and buttons, etc. - not needed.

* We need to develop 3 websites, so we are looking for a long term cooperation.
Looking forward to your creativity =)

Must Have:
Clear, intuitive structure of web pages.
In the center - of pictures reflecting our main services (industrial theme). May be in rotation.
BUT! This banner (central picture) should not be a huge one =)
All relevant information should be visible at once without scrolling.

A possibility to place media files (presentations, video ...) and 2 banner links on the main page.

Font should be available in Cyrillic.
Updates

IMPORTANT!

Please notice that in thisdesign we don't need "cleaning" and "engeneering" on this site.

So don't use old block of 4pictures from our current website. We don't need it anymore. 

Thestructure of our company has changed and now we need some links (may be banners,may be something else) to our future cleaning website as well as engeneeringwebsite.
It should look like seperate (partner) companies, not like our sevices.

Regards, Vera.

Please don't forget that we need bilingual site.

So define language changing tool in your designs.

Industry/Entity Type

Industrial

```html
<!DOCTYPE html>
<html lang="en">
<head>
<meta charset="utf-8">
<title>Brantel Group — Integrated Facility Management</title>
<link rel="stylesheet" href="https://fonts.googleapis.com/css2?family=Roboto+Condensed:wght@400;700&family=Arimo:wght@400&display=swap">
<style>
:root{
  --page:#f7f7f7;
  --stripe:#efefef;
  --lime:#dbe48c;
  --lime-light:#e9efb2;
  --olive:#7d8c27;
  --olive-dark:#87964a;
  --ink:#111111;
  --text:#6a6a6a;
  --rule:#d8d8d8;
  --white:#ffffff;
}
*{margin:0;padding:0;box-sizing:border-box}
html,body{width:1200px;height:825px;overflow:hidden}
body{
  background:var(--page) repeating-linear-gradient(135deg,var(--page) 0 3px,var(--stripe) 3px 4px);
  font-family:"Arimo",Arial,sans-serif;color:var(--text);
}
.site{position:relative;width:1200px;height:825px}

/* header */
.header{position:absolute;left:0;top:0;width:1200px;height:112px;background:var(--white);border-bottom:2px solid var(--rule)}
.brand{position:absolute;left:56px;top:22px;display:flex;align-items:center;gap:14px}
.brand-mark{width:26px;height:26px;background:var(--lime)}
.brand-name{font-family:"Roboto Condensed",Arial,sans-serif;font-weight:400;font-size:46px;letter-spacing:6px;color:var(--ink);line-height:1}
.lang{position:absolute;left:1002px;top:0;width:144px;height:30px;background:var(--lime);border-radius:0 0 8px 8px;box-shadow:0 2px 3px rgba(0,0,0,.15);display:flex;justify-content:center;gap:8px;padding-top:6px}
.lang a{font-family:"Roboto Condensed",Arial,sans-serif;font-size:16px;color:var(--ink);text-decoration:none;padding:0 8px}
.lang a.is-active{background:var(--lime-light)}
.phone{position:absolute;right:52px;top:50px;display:flex;align-items:center;gap:14px}
.phone-number{font-family:"Roboto Condensed",Arial,sans-serif;font-size:31px;color:var(--ink);letter-spacing:1px}

/* nav */
.nav{position:absolute;left:0;top:120px;width:1200px;height:43px;background:var(--lime);border-top:1px solid #c9d27a;border-bottom:1px solid #c9d27a}
.nav ul{list-style:none;display:flex;position:absolute;left:52px;top:12px}
.nav li{font-family:"Roboto Condensed",Arial,sans-serif;font-size:17px;color:var(--ink);padding:0 26px;border-left:1px solid #aab45e;line-height:19px}
.nav li:first-child{padding-left:0;border-left:0}
.search{position:absolute;left:912px;top:6px;width:195px;height:30px;background:var(--olive-dark);border:1px solid #6e7b36}
.search span{position:absolute;left:13px;top:7px;font-family:"Roboto Condensed",Arial,sans-serif;font-size:13px;font-weight:700;color:var(--white)}
.search svg{position:absolute;right:-2px;top:-3px}

/* banner */
.banner{position:absolute;left:53px;top:174px;width:1093px;height:273px;background:var(--white);border:3px solid #dedede}
.banner-photo{position:absolute;left:0;top:0;width:590px;height:267px;background:linear-gradient(90deg,#9a9a98 0%,#c9c8c3 45%,#b4bac6 70%,#ffffff 100%)}
.banner-title{position:absolute;right:52px;top:22px;text-align:right;font-family:"Roboto Condensed",Arial,sans-serif;font-size:37px;line-height:42px;color:var(--olive);letter-spacing:1px}
.banner-text{position:absolute;left:623px;top:126px;width:418px;font-family:"Roboto Condensed",Arial,sans-serif;font-size:15px;line-height:27px;letter-spacing:.6px;text-transform:uppercase;text-align:justify;color:#6d6d6d}

/* news */
.news-tab{position:absolute;left:68px;top:465px;width:92px;height:36px;background:var(--lime);border:3px solid #eef2c4;border-bottom:0;font-size:16px;color:var(--ink);text-align:center;padding-top:8px}
.news{position:absolute;left:58px;top:505px;width:302px;height:214px;background:var(--white);border:1px solid #e2e2e2;padding:8px 8px 0 30px;list-style:none}
.news li{position:relative;font-size:14px;line-height:20px;text-align:justify;color:#555;height:60px;overflow:hidden;margin-bottom:14px}
.news li::after{content:"";position:absolute;left:0;right:0;bottom:0}
.news li::before{content:"";position:absolute;left:-20px;top:6px;border-left:6px solid #777;border-top:4px solid transparent;border-bottom:4px solid transparent}
.news-rule{position:absolute;left:88px;width:264px;height:1px;background:#bbb}

/* welcome */
.welcome{position:absolute;left:390px;top:464px;width:470px}
.welcome h1{font-family:"Roboto Condensed",Arial,sans-serif;font-weight:400;font-size:21px;line-height:27px;color:var(--olive);letter-spacing:.6px}
.features{list-style:none;margin-top:19px}
.features li{position:relative;padding-left:16px;font-size:14px;line-height:20px;color:#555}
.features li::before{content:"";position:absolute;left:3px;top:6px;border-left:5px solid #888;border-top:4px solid transparent;border-bottom:4px solid transparent}
.welcome p{margin-top:20px;font-size:14px;line-height:20px;text-align:justify;color:#666}
.welcome p a{color:var(--ink)}

/* video */
.video-head{position:absolute;left:885px;top:465px;width:261px;display:flex;align-items:center;gap:6px;font-size:19px;color:#555}
.video-head::before,.video-head::after{content:"";flex:1;height:3px;background:var(--lime)}
.video{position:absolute;left:881px;top:494px;width:269px;height:234px;border:1px solid var(--ink);background:var(--white);padding:2px}
.video-frame{position:relative;width:100%;height:100%;background:radial-gradient(ellipse at 60% 40%,#6c6c6c,#3e3e3e 75%)}
.video-frame svg{position:absolute;left:98px;top:84px}

/* footer */
.footer{position:absolute;left:0;top:740px;width:1200px;height:71px;background:var(--lime)}
.footer-links{list-style:none;display:flex;justify-content:center;margin-top:14px;font-size:14px;color:var(--ink)}
.footer-links li{padding:0 12px;border-left:1px solid var(--ink);line-height:14px}
.footer-links li:first-child{border-left:0}
.copyright{text-align:center;font-size:12px;color:var(--ink);margin-top:12px}
</style>
</head>
<body>
<div class="site">
  <header class="header">
    <div class="brand"><span class="brand-mark"></span><span class="brand-name">BRANTEL GROUP</span></div>
    <nav class="lang" aria-label="Language"><a href="#">RUS</a><a href="#" class="is-active">ENG</a></nav>
    <div class="phone">
      <svg width="26" height="36" viewBox="0 0 26 36" aria-hidden="true">
        <rect x="1" y="1" width="24" height="34" rx="3" fill="#111"/>
        <rect x="5" y="5" width="16" height="9" fill="#fff"/>
        <g fill="#fff"><rect x="5" y="18" width="4" height="3"/><rect x="11" y="18" width="4" height="3"/><rect x="17" y="18" width="4" height="3"/><rect x="5" y="23" width="4" height="3"/><rect x="11" y="23" width="4" height="3"/><rect x="17" y="23" width="4" height="3"/><rect x="5" y="28" width="4" height="3"/><rect x="11" y="28" width="4" height="3"/><rect x="17" y="28" width="4" height="3"/></g>
      </svg>
      <span class="phone-number">+7 812 555 0148</span>
    </div>
  </header>

  <nav class="nav" aria-label="Main">
    <ul><li>HOME</li><li>ABOUT US</li><li>HISTORY</li><li>SERVICES</li><li>PORTFOLIO</li><li>JOBS</li><li>CONTACT US</li></ul>
    <div class="search"><span>SEARCH...</span>
      <svg width="36" height="34" viewBox="0 0 36 34" aria-hidden="true"><circle cx="21" cy="13" r="9" fill="none" stroke="#111" stroke-width="3.5"/><line x1="14" y1="20" x2="5" y2="30" stroke="#111" stroke-width="5" stroke-linecap="round"/></svg>
    </div>
  </nav>

  <section class="banner">
    <div class="banner-photo" role="img" aria-label="Photo of an industrial pump room with steel tanks and a blue pump"></div>
    <h2 class="banner-title">INTEGRATED FACILITY<br>MANAGEMENT</h2>
    <p class="banner-text">Lorem ipsum dolor sit amet, consectetur adipiscing elit. Donec adipiscing dolor a magna consequat dapibus. Praesent non ante id nisi aliquam placerat. Phasellus porta vulputate bibendum.</p>
  </section>

  <div class="news-tab">NEWS</div>
  <ul class="news">
    <li>Lorem ipsum dolor sit amet, consectetur adipiscing elit. Donec adipiscing dolor a magna consequat dapibus. Praesent non</li>
    <li>Lorem ipsum dolor sit amet, consectetur adipiscing elit. Donec adipiscing dolor a magna consequat dapibus. Praesent non</li>
    <li>Lorem ipsum dolor sit amet, consectetur adipiscing elit. Donec adipiscing dolor a</li>
  </ul>
  <div class="news-rule" style="top:580px"></div>
  <div class="news-rule" style="top:654px"></div>

  <section class="welcome">
    <h1>WELCOME TO BRANTEL GROUP<br>ENGINEERING SYSTEMS</h1>
    <ul class="features">
      <li>Commercial property management</li>
      <li>Complex maintenance of immovable property</li>
      <li>Commercial property maintenance service</li>
    </ul>
    <p>These are the most important aspects of acquisition of the highest possible incomes from the commercial property object`s operation regardless of their purpose: it can be production, business center, a building of a shop, bank, restaurant, warehousing logistic complex, hotel or the biggest shopping and recreation center. <a href="#">More...</a></p>
  </section>

  <div class="video-head">VIDEO</div>
  <div class="video">
    <div class="video-frame" role="img" aria-label="Video still of an engineer's hand drafting a technical drawing">
      <svg width="66" height="66" viewBox="0 0 66 66" aria-hidden="true"><circle cx="33" cy="33" r="31" fill="#222" stroke="#bbb" stroke-width="3"/><path d="M27 22 L42 33 L27 44 Z" fill="#fff"/></svg>
    </div>
  </div>

  <footer class="footer">
    <ul class="footer-links">
      <li>Company</li><li>Chosen by</li><li>Contact us</li><li>Integrated facility management</li><li>Technical maintenance of engineering systems</li><li>Company policy</li>
    </ul>
    <p class="copyright">All rights reserved @ brantel-group.ru</p>
  </footer>
</div>
</body>
</html>
```